Tidewell Partners Inc.
Business Card & Stationary
Tidewell Partners Inc. -
Creative Brief
Professional
Derek Holloway
President & CEO
47 Quillfern Lane Brookhaven, ON, Canada M4R 7P9
derek@tidewellpartners.example
www.tidewellpartners.example
needs to be top drawer, classy, printing costs not a key factor
Guiding Leaders Toward Steady Gains in Revenue

```html
<!DOCTYPE html>
<html lang="en">
<head>
<meta charset="utf-8">
<title>Tidewell Partners Inc. — Stationery</title>
<link rel="stylesheet" href="https://fonts.googleapis.com/css2?family=Questrial&display=swap">
<style>
:root{
  --navy:#0e3a86;
  --blue:#1560b8;
  --sky:#2f9be0;
  --grey:#a7a9ac;
  --ink:#1f3f7a;
  --paper:#ffffff;
  --edge:#d9dbde;
}
*{margin:0;padding:0;box-sizing:border-box}
html,body{width:1200px;height:1011px;overflow:hidden;background:var(--paper)}
body{position:relative;font-family:"Questrial",sans-serif;color:var(--ink)}
.sheet{position:absolute;background:var(--paper);border:1px solid var(--edge);box-shadow:0 1px 4px rgba(0,0,0,.12)}
.brand{position:absolute;display:flex;flex-direction:column;align-items:flex-start;gap:10px}
.brand-mark{width:62px;height:62px;background:var(--blue);border-radius:4px}
.brand-name{font-size:24px;color:var(--blue);white-space:nowrap}
.band{position:absolute;left:0;right:0;background:linear-gradient(90deg,var(--navy),var(--sky) 45%,var(--navy))}
.band-thin{position:absolute;left:0;right:0;height:3px;background:var(--grey)}
.contact{position:absolute;text-align:right;font-size:11px;line-height:1.55;color:var(--ink);font-style:normal}

/* letterhead */
.letterhead{left:120px;top:80px;width:737px;height:906px}
.letterhead .brand{left:38px;top:50px}
.letterhead .contact{right:48px;top:48px}
.letterhead .band{top:834px;height:34px}
.letterhead .band-thin{top:826px}

/* envelope front */
.envelope{left:86px;top:349px;width:777px;height:331px}
.envelope .brand{left:22px;top:30px}
.envelope .brand-name{font-size:28px}
.envelope .return{position:absolute;left:22px;top:270px;font-size:11px}
.envelope .band-thin{top:290px}
.envelope .band{top:301px;height:28px}

/* envelope back */
.envelope-back{position:absolute;left:86px;top:686px;width:777px;height:171px}
.envelope-back svg{display:block}

/* cards */
.card{width:280px;height:165px;left:906px}
.card-front{top:349px}
.card-back{top:534px}
.card .brand{left:50%;transform:translateX(-50%);align-items:center;gap:6px}
.card .brand-mark{width:40px;height:40px}
.card .brand-name{font-size:17px}
.card-front .brand{top:12px}
.card-back .brand{top:30px}
.card .holder{position:absolute;left:0;right:0;top:94px;text-align:center;font-size:11px;line-height:1.4}
.card .holder small{display:block;font-size:8px}
.card .details{position:absolute;left:0;right:0;top:126px;text-align:center;font-size:7px;line-height:1.5}
.card .tagline{position:absolute;left:0;right:0;top:112px;text-align:center;font-size:10.5px;color:var(--blue)}
.card .band-thin{top:auto;bottom:0;height:4px;background:linear-gradient(90deg,var(--navy),var(--sky),var(--navy))}
</style>
</head>
<body>

<section class="sheet letterhead" aria-label="Letterhead">
  <div class="brand">
    <div class="brand-mark"></div>
    <div class="brand-name">Tidewell Partners Inc.</div>
  </div>
  <address class="contact">
    47 Quillfern Lane<br>
    Brookhaven, ON, Canada, M4R 7P9<br>
    Phone: 555-010-0140<br>
    Cell: 555-010-0172<br>
    Fax: 555-010-0199<br>
    www.tidewellpartners.example
  </address>
  <div class="band-thin"></div>
  <div class="band"></div>
</section>

<section class="envelope-back" aria-label="Envelope back">
  <svg width="777" height="171" viewBox="0 0 777 171">
    <defs>
      <linearGradient id="flap" x1="0" y1="0" x2="0" y2="1">
        <stop offset="0" stop-color="#b3b5b8"/>
        <stop offset="1" stop-color="#96989b"/>
      </linearGradient>
    </defs>
    <path d="M0 0H777V40Q777 58 750 70L420 165Q388 174 356 165L27 70Q0 58 0 40Z" fill="url(#flap)"/>
    <rect x="360" y="14" width="58" height="58" rx="4" fill="#1560b8"/>
  </svg>
</section>

<section class="sheet envelope" aria-label="Envelope front">
  <div class="brand">
    <div class="brand-mark"></div>
    <div class="brand-name">Tidewell Partners Inc.</div>
  </div>
  <div class="return">47 Quillfern Lane, Brookhaven, ON, Canada, M4R 7P9</div>
  <div class="band-thin"></div>
  <div class="band"></div>
</section>

<section class="sheet card card-front" aria-label="Business card front">
  <div class="brand">
    <div class="brand-mark"></div>
    <div class="brand-name">Tidewell Partners Inc.</div>
  </div>
  <div class="holder">Derek Holloway<small>President &amp; CEO</small></div>
  <div class="details">
    47 Quillfern Lane, Brookhaven, ON, Canada M4R 7P9<br>
    Phone: 555-010-0140 | Cell: 555-010-0172 | Fax: 555-010-0199<br>
    derek@tidewellpartners.example | www.tidewellpartners.example
  </div>
  <div class="band-thin"></div>
</section>

<section class="sheet card card-back" aria-label="Business card back">
  <div class="brand">
    <div class="brand-mark"></div>
    <div class="brand-name">Tidewell Partners Inc.</div>
  </div>
  <div class="tagline">Guiding Leaders Toward Steady Gains in Revenue</div>
  <div class="band-thin"></div>
</section>

</body>
</html>
```